Renewable energy company needs modern memorable marketing brochure

We have an 8 page marketing brochure which was created in house. This needs to be revamped and modernised to stand out from our competitors in Australia, Chile and the UK. The brochure should depict us as a professional and dynamic company and instil confidence in prospective clients that we do a professional job. Once the design is finalised we will need a country specific document in the correct language i.e. Spanish for Chile. We are happy to pay for these iterations. We have a company logo which we would like incorporated into the brochure and the colours from the logo utilised where appropriate in the overall design. I have uploaded our existing brochure for an example of the content that the brochure needs to have and can upload the images separately if they are needed. Images in the brochure need to be copyright free and we have lots of photos in-house. I have added all the images from the last brochure and also the text in Indesign so it can be copied easily if needed.

Target Market(s)

landowners and companies

Industry/Entity Type

It Company

Requirements
Must have
• A clean modern look with some colours taken from the logo colour. Be easy to print in various countries.

```html
<!DOCTYPE html>
<html lang="en">
<head>
<meta charset="utf-8">
<title>Overview of Landowner Agreements – Brochure Spread</title>
<link href="https://fonts.googleapis.com/css2?family=Ubuntu:wght@300;400;500;700&family=PT+Sans:ital,wght@0,400;0,700;1,700&display=swap" rel="stylesheet">
<style>
  :root{
    --teal:#22a58c;
    --teal-text:#1aa28a;
    --ink:#3f3f3f;
    --body:#3a3a3a;
    --paper:#ffffff;
    --header-grey:#f2f2f2;
    --backdrop:#e4e6e8;
    --rule:#9a9a9a;
  }
  *{box-sizing:border-box;margin:0;padding:0}
  html,body{width:1200px;height:1200px;overflow:hidden;background:var(--backdrop)}
  body{position:relative;font-family:"PT Sans",Arial,sans-serif;color:var(--body)}

  .spread{position:absolute;left:40px;top:206px;width:1120px;height:787px;background:var(--paper);box-shadow:0 6px 18px rgba(0,0,0,.18)}
  .page-left{position:absolute;left:0;top:0;width:564px;height:787px;overflow:hidden}
  .page-right{position:absolute;left:564px;top:0;width:556px;height:787px;overflow:hidden}

  /* left page */
  .page-header{position:absolute;left:0;top:0;width:564px;height:120px;
    background:repeating-linear-gradient(135deg,#f6f6f6 0 3px,#efefef 3px 6px)}
  .page-title{position:absolute;left:20px;top:26px;font-family:"Ubuntu",sans-serif;line-height:1.12}
  .page-title .lead{display:block;font-weight:700;font-size:29px;color:var(--ink);letter-spacing:.5px}
  .page-title .main{display:block;font-weight:300;font-size:31px;color:var(--teal-text);letter-spacing:.3px}

  .steps{position:absolute;left:0;top:120px;width:303px;height:667px;background:var(--teal)}
  .step{position:absolute;left:0;width:303px;height:167px;color:#fff}
  .step-icon{position:absolute;left:16px;width:44px;height:44px}
  .step-body{position:absolute;left:92px;right:14px}
  .step-title{font-weight:700;font-size:14.5px;line-height:1.1;margin-bottom:4px}
  .step-title .indent{display:block;padding-left:17px}
  .step-text{font-size:10.5px;line-height:13.4px}
  .dividers{position:absolute;left:0;top:120px;width:303px;height:667px;pointer-events:none}

  .photo{position:absolute;left:303px;width:261px}
  .photo-panels{top:120px;height:335px;
    background:linear-gradient(180deg,#b9c3c6 0%,#8e989a 28%,#6f8f55 55%,#4f7e2e 100%)}
  .photo-inverter{top:455px;height:332px;
    background:linear-gradient(180deg,#e5e8e8 0%,#c6cbcc 35%,#a9b0ac 60%,#6f8a4a 82%,#5a7a36 100%)}

  /* right page */
  .map{position:absolute;left:0;top:0;width:556px;height:212px;
    background:radial-gradient(ellipse at 55% 40%,#c0281a 0%,#e2461a 30%,#f07a18 55%,#f6b21a 75%,#8fce2a 92%,#2fa84a 100%)}
  .section-band{position:absolute;left:49px;top:200px;width:455px;height:34px;background:var(--teal);
    color:#fff;font-family:"Ubuntu",sans-serif;font-weight:300;font-size:19px;text-align:center;line-height:34px;letter-spacing:.3px}
  .intro{position:absolute;left:24px;top:246px;width:515px;font-size:12.3px;line-height:19px;text-align:justify}
  .process-title{position:absolute;left:24px;top:396px;font-family:"Ubuntu",sans-serif;font-weight:500;font-size:20px;color:var(--teal-text)}
  .stage{position:absolute;width:240px}
  .stage-num{font-family:"Ubuntu",sans-serif;font-weight:500;font-size:15px;color:var(--ink)}
  .stage-name{font-weight:700;font-style:italic;font-size:11.5px;color:var(--teal-text);margin:1px 0 6px}
  .stage-text{font-size:10.2px;line-height:13.6px;text-align:justify}
  .stage-rule{position:absolute;top:583px;width:240px;height:1px;background:var(--rule)}
</style>
</head>
<body>
<div class="spread">

  <section class="page-left">
    <header class="page-header">
      <h1 class="page-title"><span class="lead">OVERVIEW OF</span><span class="main">LANDOWNER AGREEMENTS</span></h1>
    </header>

    <div class="steps">
      <div class="step" style="top:0">
        <svg class="step-icon" style="top:52px" viewBox="0 0 44 44" fill="none" stroke="#fff" stroke-width="2.4">
          <path d="M8 8h28v8H8z"/><path d="M6 16h32v20H6z"/><path d="M16 22h12v4H16z"/>
        </svg>
        <div class="step-body" style="top:34px">
          <h2 class="step-title">1. Heads of Terms</h2>
          <p class="step-text">We will propose headline commercial and other contractual terms to you in a non-binding Heads of Terms document. As part of this document, an exclusivity agreement must also be enacted.</p>
        </div>
      </div>

      <div class="step" style="top:167px">
        <svg class="step-icon" style="top:46px" viewBox="0 0 44 44" fill="#fff">
          <circle cx="22" cy="17" r="12"/>
          <circle cx="22" cy="17" r="8" fill="#22a58c"/>
          <path d="M22 11.5l1.7 3.6 3.9.4-2.9 2.6.8 3.9-3.5-2-3.5 2 .8-3.9-2.9-2.6 3.9-.4z"/>
          <path d="M14 26l-6 12 5-1 3 4 5-11zM30 26l6 12-5-1-3 4-5-11z"/>
        </svg>
        <div class="step-body" style="top:33px">
          <h2 class="step-title">2. Exclusivity</h2>
          <p class="step-text">This agreement is valid for a limited period of time (usually a year) and ensures that Brightvale has the sole rights to the parcel of land that the solar farm will be situated upon.</p>
        </div>
      </div>

      <div class="step" style="top:334px">
        <svg class="step-icon" style="top:52px" viewBox="0 0 44 44" fill="none" stroke="#fff" stroke-width="2.4">
          <path d="M16 8h14l8 8v22H22"/><path d="M30 8v8h8"/><path d="M16 8v14"/>
          <circle cx="13" cy="32" r="4.5"/><path d="M13 23v3M13 38v3M4 32h3M19 32h3M7 26l2 2M17 36l2 2M7 38l2-2M17 28l2-2"/>
        </svg>
        <div class="step-body" style="top:30px">
          <h2 class="step-title">3. Option Agreement</h2>
          <p class="step-text">Once project feasibility has been demonstrated, at our cost we will instruct lawyers to negotiate the option agreement with your lawyers. The lease will run for an agreed period of time and come into force once construction begins.</p>
        </div>
      </div>

      <div class="step" style="top:501px">
        <svg class="step-icon" style="top:48px" viewBox="0 0 44 44" fill="#fff">
          <path d="M2 18l8-6 4 3-8 10z"/><path d="M42 18l-8-6-4 3 8 10z"/>
          <path d="M13 15l7-3 5 2 7-1 5 10-9 10-4 3-3-1-3 1-9-11z"/>
          <path d="M20 16l-4 4 3 2 6-4" fill="#22a58c"/>
        </svg>
        <div class="step-body" style="top:24px">
          <h2 class="step-title">4. Exercising the Option<span class="indent">to Lease</span></h2>
          <p class="step-text">The lease will allow us to construct, operate and decommission the solar farm within a certain time frame. Committing to the Lease will also ensure that we pay you an inflation linked rent for the lifetime of the solar farm.</p>
        </div>
      </div>
    </div>

    <svg class="dividers" viewBox="0 0 303 667">
      <path d="M0 0h184l18 14 18-14h83" fill="none" stroke="#fff" stroke-width="3"/>
      <path d="M0 167h184l18 14 18-14h83" fill="none" stroke="#fff" stroke-width="3"/>
      <path d="M0 334h184l18 14 18-14h83" fill="none" stroke="#fff" stroke-width="3"/>
      <path d="M0 501h184l18 14 18-14h83" fill="none" stroke="#fff" stroke-width="3"/>
    </svg>

    <div class="photo photo-panels" role="img" aria-label="Photograph looking along rows of raised solar panels over tall green grass"></div>
    <div class="photo photo-inverter" role="img" aria-label="Photograph of a grey inverter cabinet standing on grass beside solar panel rows"></div>
  </section>

  <section class="page-right">
    <div class="map" role="img" aria-label="World map heat chart of solar irradiation, red and orange over the continents fading to green"></div>
    <h2 class="section-band">SOLAR IN AUSTRALIA</h2>
    <p class="intro">Australia is blessed with abundant sunshine. In fact, it’s the sunniest continent on Earth, and consequently boasts some of the best levels of solar irradiation. Each year Australia receives 10,000 times the amount of energy that it currently uses. This means that all of Australia’s energy needs could be met if solar farms covered only 0.05% of the land mass. Australia’s climate provides the country with a huge opportunity to produce clean and sustainable renewable energy from an infinate resource, the sun.</p>

    <h2 class="process-title">THE PROCESS</h2>

    <div class="stage" style="left:24px;top:430px">
      <h3 class="stage-num">Stage 1</h3>
      <p class="stage-name">Exclusivity Agreement &amp; Heads of Terms</p>
      <p class="stage-text">In order to ensure we are the only entity using a particular piece of land, we require the exclusive legal rights over it. Once this has been agreed, we will proceed with a grid application to the Network Service Provider whilst beginning the process of conducting environmental and other feasibility studies.</p>
    </div>
    <div class="stage" style="left:295px;top:430px">
      <h3 class="stage-num">Stage 3</h3>
      <p class="stage-name">Lease</p>
      <p class="stage-text">With development permission granted and the grid connection secured, we will ask that you enter into a Lease agreement, rental payments will be paid to the landowner on an hectarage used basis. Construction takes between 8 – 12 weeks and once complete, the solar farm will be operational for a minimum of 25 years.</p>
    </div>

    <div class="stage-rule" style="left:24px"></div>
    <div class="stage-rule" style="left:295px"></div>

    <div class="stage" style="left:24px;top:603px">
      <h3 class="stage-num">Stage 2</h3>
      <p class="stage-name">Development Approval</p>
      <p class="stage-text">Once the option has been agreed environmental studies will be undertaken and we will hold a public consultation event, where the local community can become involved in the development of the project. Following the results of the consultation event and environmental studies a development application will be sent to the Council. During this time we will negotiate the Option to Lease documentation.</p>
    </div>
    <div class="stage" style="left:295px;top:603px">
      <h3 class="stage-num">Stage 4</h3>
      <p class="stage-name">Decommissioning</p>
      <p class="stage-text">The solar farm, its equipment and infrastructure will be removed entirely and the site restored to its former condition.</p>
    </div>
  </section>

</div>
</body>
</html>
```